Kestrel Homes Australia Business Card

We need a Business Card design for our new start up company.
A unique model designed to address Australia’s growing housing affordability problem has been launched. More than half of Australians are being priced out of the property market and have resigned themselves to the fact that they may never be able to afford a home.
We have developed a unique Algorithm that allows people to get into property and reverse this trend of domination by the property investors in this country. The first of its kind model facilitates connecting people to lending facilities that do not require them to have the finance combined under the purchase contract.
Ownership is shared with a second-tier investor, made up of either family or friends if not, Kestrel Homes Australia will provide a mini property investor enabling thousands of people the opportunity to buy a home, which they otherwise thought was not possible.
Kestrel Homes Australia is addressing housing affordability for families and individuals, giving every Australian looking to buy a home the opportunity to enter the property market to live in or invest.
Under our unique model, there is no combined finance, and individuals are assessed for their percentage portion of the property only. “A unique feature of our product is it is based around the strategies used for property investment. I have developed a unique Algorithm that enables the Home buyer to purchase 60% of a property, while Kestrel Homes Australia facilitates a second-tier investor to buy the other 40%. The Algorithm locks the investor in place and enables the home buyer to stairway to full ownership. The investment is secured against real property.
Please refer to our website www.kestrelhomes.com.au for inspiration.
Also please find attached our logo.
Any further directions please ask.
Cheers Marcus
Industry/Entity Type
Real Estate
Contact Information for Business Card
Marcus Thorley
CEO
Mobile 0400 615 272
www.kestrelhomes.com.au
Email: marcus@kestrelhomes.com.au
Colors
Designer to choose colors to be used in the design.
Look and feel

```html
<!DOCTYPE html>
<html lang="en">
<head>
<meta charset="utf-8">
<title>Kestrel Homes Australia – Business Card</title>
<link href="https://fonts.googleapis.com/css2?family=Montserrat:wght@400;500;700;800&display=swap" rel="stylesheet">
<style>
  :root {
    --stage: #4a4c4f;
    --brand-green: #3aac48;
    --brand-green-dark: #2f9a3c;
    --brand-blue: #1e9fd6;
    --ink: #3a3a3a;
    --paper: #ffffff;
  }
  * { box-sizing: border-box; margin: 0; padding: 0; }
  html, body {
    width: 1200px; height: 1000px; overflow: hidden;
    background: var(--stage);
    font-family: "Montserrat", Arial, sans-serif;
  }
  .canvas { position: relative; width: 1200px; height: 1000px; }

  .card {
    position: absolute; width: 600px; height: 343px;
    border-radius: 4px; overflow: hidden;
    box-shadow: 0 12px 30px rgba(0,0,0,.35);
  }

  /* Front */
  .card--front { left: 110px; top: 110px; background: var(--brand-green); color: var(--paper); text-align: center; }
  .front__brand { position: absolute; left: 0; right: 0; top: 112px; }
  .brand-name { font-weight: 800; font-size: 26px; letter-spacing: .2px; white-space: nowrap; }
  .brand-name .dot {
    display: inline-block; width: 14px; height: 14px; border-radius: 50%;
    background: currentColor; margin-right: 8px; vertical-align: 1px;
  }
  .brand-tagline { font-weight: 700; font-size: 13px; margin-top: 6px; white-space: nowrap; }
  .front__web { position: absolute; left: 0; right: 0; bottom: 58px; font-size: 17px; letter-spacing: .8px; font-weight: 500; }

  /* Back */
  .card--back { left: 490px; top: 530px; background: var(--paper); color: var(--ink); }
  .back__tab {
    position: absolute; left: -10px; top: 196px; width: 24px; height: 52px;
    background: var(--brand-green); border-radius: 8px;
  }
  .back__person { position: absolute; left: 42px; top: 196px; }
  .person-name { color: var(--brand-green); font-weight: 800; font-size: 28px; letter-spacing: .3px; white-space: nowrap; }
  .person-role { font-size: 17px; font-weight: 500; margin-top: 2px; }

  .back__brand { position: absolute; right: 30px; top: 34px; text-align: center; }
  .back__brand .brand-name { color: var(--brand-blue); font-size: 20px; }
  .back__brand .brand-tagline { color: var(--brand-green-dark); font-size: 10.5px; margin-top: 3px; }

  .back__address { position: absolute; left: 350px; top: 128px; font-size: 14px; line-height: 1.4; font-style: normal; }
  .back__contacts { position: absolute; left: 350px; top: 196px; list-style: none; font-size: 14px; }
  .back__contacts li { display: flex; align-items: center; gap: 10px; line-height: 23px; white-space: nowrap; }
  .back__contacts svg { width: 13px; height: 13px; fill: var(--brand-green); flex: none; }
  .accent { color: var(--brand-green); }
</style>
</head>
<body>
<main class="canvas">

  <section class="card card--front" aria-label="Business card front">
    <div class="front__brand">
      <div class="brand-name"><span class="dot"></span>Kestrel Homes Australia</div>
      <div class="brand-tagline">Helping Buyers Reach Their Homes</div>
    </div>
    <div class="front__web">www.kestrelhomes.com.au</div>
  </section>

  <section class="card card--back" aria-label="Business card back">
    <span class="back__tab"></span>

    <div class="back__brand">
      <div class="brand-name">Kestrel Homes Australia</div>
      <div class="brand-tagline">Helping Buyers Reach Their Homes</div>
    </div>

    <div class="back__person">
      <div class="person-name">MARCUS THORLEY</div>
      <div class="person-role">Founder/CEO</div>
    </div>

    <address class="back__address">
      Your Street Address,<br>Australia, 1234
    </address>

    <ul class="back__contacts">
      <li>
        <svg viewBox="0 0 24 24"><path d="M6.6 10.8a15.1 15.1 0 0 0 6.6 6.6l2.2-2.2a1 1 0 0 1 1-.25 11.4 11.4 0 0 0 3.6.57 1 1 0 0 1 1 1V20a1 1 0 0 1-1 1A17 17 0 0 1 3 4a1 1 0 0 1 1-1h3.5a1 1 0 0 1 1 1c0 1.25.2 2.450.57 3.6a1 1 0 0 1-.25 1z"/></svg>
        0400615272
      </li>
      <li>
        <svg viewBox="0 0 24 24"><path d="M2 5h20v2l-10 6L2 7z"/><path d="M2 9l10 6 10-6v10H2z"/></svg>
        marcus@kestrelhomes.com.au
      </li>
      <li>
        <svg viewBox="0 0 24 24"><circle cx="12" cy="12" r="10"/></svg>
        <span>www.<span class="accent">kestrelhomes</span>.com.au</span>
      </li>
    </ul>
  </section>

</main>
</body>
</html>
```